Shelter is Kindred Warmth Fact Sheet (2 sided page)

We are looking to create a 2-page Fact Sheet (front and back)
- The head logo is going to be: Shelter is Kindred Warmth
- The title of the fact sheet will be: Get the Facts on Mpox Vaccination
- Please include RK7's logo - please make sure there is room for another logo next to this (this is not included at this time)
- Use the colors and font and mimic the feel of our past resources from ravenkinship.org/resources
- The main image should be incorporated for design (this is the beading circle image with 3 people beading) - additional images (feather & braided sweetgrass) can be included as needed for elements
- Do not put text over graphics and keep it simple and easy to read with high contrast.
- We want some very simple design element(s) incorporated that convey Native American communities or heritage. But NO headdress, teepee graphics, etc.
- Ensure that linked text remains in document for virtual use
- Please include this list before the funding statement - For more information, please visit:
www.ravenkinship.org/vaccines
www.bolderpath.org/campaigns/mpox/
www.nwho.example/poxvirus/mpox/
- Please remember to include the funding statement - it can be in a very small font 6/7 point. "This project: Joining Hands with Regional Allies to Strengthen Neighborhood-Led Groups to Broaden Immunization Reach Among Diverse Cultural and Heritage Grown-Up Groups Presently Facing Gaps is supported by the Bureau for Illness Tracking and Safeguarding (BITS) of the Federal Office of Wellness and Social Services (OWS) as part of a financial assistance award totaling $5,000,000 with 100 percent funded by BITS/OWS. The contents are those of the author(s) and do not necessarily represent the official views of, nor an endorsement by, BITS/OWS or the U.S. Government. "

Target Market(s)

American Indian and Alaska Native Two Spirit Indigiqueer

Requirements
Must have
• Worldwide Council for Native Elders (RK7) color scheme - see website

```html
<!DOCTYPE html>
<html lang="en">
<head>
<meta charset="utf-8">
<title>Shelter is Kindred Warmth – Mpox Vaccination Fact Sheet</title>
<link rel="stylesheet" href="https://fonts.googleapis.com/css2?family=Barlow+Condensed:wght@700;800&family=Montserrat:wght@400;600;700&display=swap">
<style>
  :root{
    --backdrop:#ece6de;
    --paper:#ffffff;
    --header-green:#5f8a3a;
    --text-green:#4e7a2a;
    --maroon:#8c4440;
    --maroon-dark:#7c3a37;
    --fact-red:#8e3b3a;
    --feather-dark:#4a3a36;
    --feather-light:#cfc9c4;
    --sweetgrass-a:#c7dc7e;
    --sweetgrass-b:#7fa84a;
  }
  *{box-sizing:border-box;margin:0;padding:0}
  html,body{width:1200px;height:736px;overflow:hidden}
  body{background:var(--backdrop);font-family:"Montserrat",Arial,sans-serif;position:relative}
  .page{position:absolute;background:var(--paper);box-shadow:4px 6px 10px rgba(0,0,0,.18);overflow:hidden}
  .page--front{left:157px;top:77px;width:420px;height:593px}
  .page--back{left:610px;top:78px;width:423px;height:592px}

  /* header */
  .masthead{position:absolute;left:0;top:0;width:420px;height:75px;display:flex}
  .masthead__art{width:90px;height:75px;background:radial-gradient(circle at 50% 55%,#e0a14a 0%,#b5503d 45%,#5d7b3a 80%)}
  .masthead__title{width:205px;height:75px;background:var(--header-green);color:#fff;font-family:"Barlow Condensed",Arial Narrow,sans-serif;text-align:center;padding-top:8px}
  .masthead__kicker{font-size:18px;font-weight:700;letter-spacing:.5px;line-height:18px;display:flex;align-items:center;justify-content:center;gap:5px}
  .masthead__name{font-size:24px;font-weight:800;line-height:25px;letter-spacing:.3px}
  .masthead__sub{font-size:10.5px;font-weight:700;line-height:14px;letter-spacing:.2px}
  .masthead__brand{flex:1;display:flex;align-items:center;gap:5px;padding-left:8px}
  .brand-mark{width:16px;height:16px;background:var(--maroon)}
  .brand-name{color:var(--maroon);font-family:"Barlow Condensed",Arial Narrow,sans-serif;font-weight:700;font-size:8.5px;line-height:9px;letter-spacing:.2px}

  .band{position:absolute;left:0;background:var(--maroon)}
  .band--top{top:75px;width:420px;height:28px}
  .band--bottom{top:564px;width:420px;height:29px}
  .band--footer{top:482px;width:423px;height:110px}

  .sweetgrass{position:absolute;background:linear-gradient(90deg,var(--sweetgrass-b),var(--sweetgrass-a) 50%,var(--sweetgrass-b))}
  .page--front .sweetgrass{left:384px;top:103px;width:34px;height:461px}
  .page--back .sweetgrass{left:390px;top:0;width:33px;height:482px}

  /* content */
  .item{position:absolute;font-size:7.2px;line-height:8.8px;color:var(--text-green)}
  .page--front .item{left:49px;width:248px}
  .page--back .item{left:66px;width:250px}
  .page--back .item--shift{left:62px}
  .fact{color:var(--fact-red);font-weight:700}
  .fact b{font-weight:700}
  .lead{font-weight:700;color:var(--fact-red)}
  .strong-green{font-weight:600}
  .feather{position:absolute;left:-27px;top:1px;width:20px;height:5px;border-radius:50%;background:linear-gradient(90deg,var(--feather-dark) 35%,var(--feather-light) 40%)}
  .page--back .feather{left:-39px}
  .dot::before{content:"";position:absolute;left:-30px;top:3px;width:2.4px;height:2.4px;border-radius:50%;background:var(--text-green)}
  .page--back .dot::before{left:-29px;background:var(--fact-red)}
  .link{color:var(--fact-red);font-weight:700;text-decoration:none}

  .funding{position:absolute;left:32px;top:38px;width:363px;color:#fff;font-size:4.8px;line-height:6.3px;text-align:center}
</style>
</head>
<body>

<section class="page page--front">
  <header class="masthead">
    <div class="masthead__art" role="img" aria-label="Illustration of three people beading together in a circle"></div>
    <div class="masthead__title">
      <div class="masthead__kicker"><span class="feather" style="position:static;width:16px" role="img" aria-label="feather"></span>SHELTER IS<span class="feather" style="position:static;width:16px" role="img" aria-label="feather"></span></div>
      <div class="masthead__name">KINDRED WARMTH</div>
      <div class="masthead__sub">GET THE FACTS ON MPOX VACCINATION</div>
    </div>
    <div class="masthead__brand">
      <span class="brand-mark"></span>
      <span class="brand-name">WORLDWIDE COUNCIL FOR<br>NATIVE ELDERS</span>
    </div>
  </header>
  <div class="band band--top" role="img" aria-label="Woven diamond pattern band"></div>
  <div class="sweetgrass" role="img" aria-label="Braided sweetgrass"></div>

  <p class="item fact" style="top:134px"><span class="feather" role="img" aria-label="feather"></span>Fact: Mpox (formerly known as monkeypox) is a serious virus that can cause rash, fever, and other symptoms.</p>
  <p class="item dot" style="top:159px;width:215px">Mpox can spread to anyone through close, personal, often skin-to-skin contact.</p>
  <p class="item fact" style="top:184px"><span class="feather" role="img" aria-label="feather"></span>Fact: Vaccines can help keep yourself, family, and community safe by stopping the spread of mpox.</p>
  <p class="item dot" style="top:208px">Vaccines are important in stopping the spread of mpox. People who are vaccinated for mpox should still continue to avoid close, skin-to-skin contact with someone who has mpox.</p>
  <p class="item fact" style="top:242px"><span class="feather" role="img" aria-label="feather"></span>Fact: The BITS recommends getting a vaccine for people 18 and older who are at risk for mpox.</p>
  <p class="item lead" style="top:267px">People at risk for mpox include:</p>
  <p class="item dot" style="top:284px">Gay, bisexual, Two Spirit, MSM (men who have sex with men), trans or gender diverse people who in the past 6 months have had one of the following:</p>
  <p class="item dot" style="top:315px">A new diagnosis of more than one sexually transmitted disease</p>
  <p class="item dot" style="top:328px">More than one sex partner</p>
  <p class="item dot" style="top:342px">Sex at a commercial sex venue</p>
  <p class="item dot" style="top:353px">Sex at a large public event where there are people who have mpox</p>
  <p class="item dot strong-green" style="top:370px">Sexual partners of persons with the risks described in above</p>
  <p class="item dot strong-green" style="top:382px">People who experience any of the above</p>
  <p class="item fact" style="top:397px"><span class="feather" role="img" aria-label="feather"></span>Fact: People with untreated HIV are more likely to get severe cases of mpox.</p>
  <p class="item dot" style="top:421px">The mpox vaccine is safe for people with HIV. Get two doses of the mpox vaccine as soon as you can. If you don’t know your HIV status, get tested.</p>
  <p class="item fact" style="top:460px"><span class="feather" role="img" aria-label="feather"></span>Fact: Two shots are better than one.</p>
  <p class="item dot" style="top:481px">VAXORA is a 2-dose vaccine that protects against mpox infections.</p>
  <p class="item dot" style="top:497px">People need to get both doses of the vaccine for the best protection against mpox, unless you had a severe allergic reaction after getting your first dose of the VAXORA vaccine.</p>
  <p class="item dot" style="top:533px">The second dose should be given 4 weeks after the first dose.</p>

  <div class="band band--bottom" role="img" aria-label="Woven diamond pattern band"></div>
</section>

<section class="page page--back">
  <div class="sweetgrass" role="img" aria-label="Braided sweetgrass"></div>

  <p class="item fact" style="top:38px"><span class="feather" role="img" aria-label="feather"></span>Fact: Already exposed to mpox? You can still get vaccinated.</p>
  <p class="item dot" style="top:53px">Get vaccinated as soon as possible after being exposed to someone with mpox (if exposed less than 14 days ago, ideally within 4 days of exposure).</p>
  <p class="item fact" style="top:92px"><span class="feather" role="img" aria-label="feather"></span>Fact: You can call the shots.</p>
  <p class="item dot" style="top:109px">Reduce scarring by asking about how and where to get the mpox vaccine on your body, such as on the back of your upper arm.</p>
  <p class="item fact" style="top:140px"><span class="feather" role="img" aria-label="feather"></span>Fact: Not everyone has side effects, but some people do.</p>
  <p class="item dot" style="top:159px">The most common side effects after the VAXORA vaccine are:</p>
  <p class="item dot" style="top:175px">Pain, redness, and itching at the spot the vaccine is given</p>
  <p class="item dot" style="top:192px">Fever, headache, tiredness, nausea, chills, and muscle aches</p>
  <p class="item dot" style="top:207px">These area signs that your immune system is responding, not that you are getting sick.</p>
  <p class="item item--shift fact" style="top:235px"><span class="feather" role="img" aria-label="feather" style="left:-35px"></span>Fact: Mpox vaccines are free.</p>
  <p class="item item--shift dot" style="top:253px"><span></span>Providers must give you the vaccine regardless of your ability to pay the administration fee. Learn more and find an mpox vaccine site near you.</p>
  <p class="item item--shift fact" style="top:289px"><span class="feather" role="img" aria-label="feather" style="left:-35px"></span>Fact: Mpox vaccines are safe and effective.</p>
  <p class="item item--shift dot" style="top:310px">Over one million vaccine doses have been given in the US with no new or unexpected safety concerns and serious adverse events to the mpox vaccine are rare. People who have been vaccinated can still get mpox, but vaccination may make illness less severe.</p>
  <p class="item item--shift dot" style="top:360px"><a class="link" href="https://www.ravenkinship.org/vaccines">www.ravenkinship.org/vaccines</a></p>
  <p class="item item--shift dot" style="top:372px"><a class="link" href="https://www.bolderpath.org/campaigns/mpox/">www.bolderpath.org/campaigns/mpox/</a></p>
  <p class="item item--shift dot" style="top:384px"><a class="link" href="https://www.nwho.example/poxvirus/mpox/">www.nwho.example/poxvirus/mpox/</a></p>

  <footer class="band band--footer">
    <p class="funding">This project: Joining Hands with Regional Allies to Strengthen Neighborhood-Led Groups to Broaden Immunization Reach Among Diverse Cultural and Heritage Grown-Up Groups Presently Facing Gaps is supported by the Bureau for Illness Tracking and Safeguarding (BITS) of the Federal Office of Wellness and Social Services (OWS) as part of a financial assistance award totaling $5,000,000 with 100 percent funded by BITS/OWS. The contents are those of the author(s) and do not necessarily represent the official views of, nor an endorsement by, BITS/OWS or the U.S. Government.</p>
  </footer>
</section>

</body>
</html>
```